Label design, for stand up guayusa tea pouch.

I need a high quality, clean, modern sticker label design. Its going on a stand up tea pouch. The front of the pouch is transparent, with a foil back. The foil back is visible from front view.The product is a dark green herb. its in the form of loose leaf tea. Guayusa provides clean energy. Its main point is that its an alternative to coffee with similar caffeine levels, but it doesn't give the same jittery feeling as coffee because of a component called theobromine.

Target Market(s)

Men and women 18-65

Font styles to use
Sans Serif
Decorative

Colors

Designer to choose colors to be used in the design.

Requirements
Must have
• -Logo provided: icon
• The logo icon colors can be changed to have some green if it will work better
• -Brand: Lanternmoss guayusa
• -A background that goes well with the packaging (transparent/foil) picture provided
Should not have
• Blank background
• Overly loud background

```html
<!DOCTYPE html>
<html lang="en">
<head>
<meta charset="utf-8">
<title>Lanternmoss guayusa – pouch label</title>
<link href="https://fonts.googleapis.com/css2?family=Alfa+Slab+One&family=Merriweather:ital,wght@0,700;1,400&family=Open+Sans:wght@600;700&display=swap" rel="stylesheet">
<style>
  :root {
    --backdrop: #e4e4e4;
    --label-cream: #fcedbb;
    --leaf-green: #7ab53c;
    --brand-green: #6aa92e;
    --ink: #1c1c1c;
    --pill-text: #f8eeb4;
  }
  html, body {
    margin: 0;
    padding: 0;
    width: 898px;
    height: 1200px;
    overflow: hidden;
    background: var(--backdrop);
  }
  .label {
    position: absolute;
    left: 89px;
    top: 50px;
    width: 720px;
    height: 1100px;
    background: var(--label-cream);
    border-radius: 40px;
    box-sizing: border-box;
  }
  .label-frame {
    position: absolute;
    left: 45px;
    top: 54px;
    width: 628px;
    height: 965px;
    border: 3px solid var(--leaf-green);
    border-radius: 36px;
    box-sizing: border-box;
  }
  .brand-name {
    position: absolute;
    left: 0;
    right: 0;
    top: 278px;
    margin: 0;
    text-align: center;
    font-family: "Open Sans", sans-serif;
    font-weight: 600;
    font-size: 30px;
    color: var(--brand-green);
  }
  .product-title {
    position: absolute;
    left: 0;
    right: 0;
    top: 360px;
    margin: 0;
    text-align: center;
    font-family: "Alfa Slab One", serif;
    font-weight: 400;
    font-size: 92px;
    letter-spacing: 3px;
    color: var(--ink);
  }
  .product-tagline {
    position: absolute;
    left: 0;
    right: 0;
    top: 494px;
    margin: 0;
    text-align: center;
    font-family: "Merriweather", serif;
    font-style: italic;
    font-size: 24px;
    color: #333;
  }
  .product-summary {
    position: absolute;
    left: 100px;
    right: 100px;
    top: 548px;
    margin: 0;
    text-align: center;
    font-family: "Merriweather", serif;
    font-weight: 700;
    font-size: 19px;
    line-height: 27px;
    color: var(--ink);
  }
  .divider {
    position: absolute;
    left: 45px;
    width: 628px;
    height: 3px;
    background: var(--leaf-green);
  }
  .divider-upper { top: 656px; }
  .divider-lower { top: 789px; }
  .brewing-note {
    position: absolute;
    left: 75px;
    right: 75px;
    top: 678px;
    margin: 0;
    text-align: justify;
    font-family: "Merriweather", serif;
    font-style: italic;
    font-size: 14px;
    line-height: 24px;
    color: #333;
  }
  .benefit-pill {
    position: absolute;
    left: 178px;
    top: 827px;
    width: 366px;
    height: 98px;
    border-radius: 49px;
    background: var(--leaf-green);
    display: flex;
    flex-direction: column;
    justify-content: center;
    align-items: center;
    font-family: "Open Sans", sans-serif;
    font-weight: 700;
    font-size: 20px;
    line-height: 27px;
    letter-spacing: 0.5px;
    color: var(--pill-text);
  }
  .net-weight {
    position: absolute;
    left: 0;
    right: 0;
    top: 942px;
    margin: 0;
    text-align: center;
    font-family: "Merriweather", serif;
    font-style: italic;
    font-size: 26px;
    color: #333;
  }
</style>
</head>
<body>
  <div class="label">
    <div class="label-frame"></div>
    <p class="brand-name">Lanternmoss tea</p>
    <h1 class="product-title">GUAYUSA</h1>
    <p class="product-tagline">ENERGIZING HERBAL TEA</p>
    <p class="product-summary">Guayusa is made from holly leaves grown in the Amazon. It is an excellent source of antioxidants and vitamins.</p>
    <div class="divider divider-upper"></div>
    <p class="brewing-note">To prepare, cold water should be boiled and then poured onto the leaves. The leaves should be allowed to steep in the water for at least four minutes for weak tea. For every 8 ounces (236 ml) of water, 2 grams of tea leaves are suggested.</p>
    <div class="divider divider-lower"></div>
    <div class="benefit-pill">
      <span>PROVIDES CLEAN ENERGY</span>
      <span>CONTENT THEOBROMINE</span>
    </div>
    <p class="net-weight">XXX gr</p>
  </div>
</body>
</html>
```